Business Card Design Project

Looking for a logo and business card for a Real State Business i will be opening. The name is not choosen yet , but will probably be RTV IMOVEIS.
I was thinking black and silver colors, but am open to nice ideas.
I did add a business card that i liked a lot, am looking for something like that, with logo in black or silver in a black card. The logo i was thinking in the letters RTV as i uploaded or something or little and cute buildings or a house...just ideas, can be any nice logo.
Updates

You guys can add other colors if you want, I like colors very "BRIGHT" and "open", like red, pink, strong colors. almost glow in the dark colors. lol

Designers,

I've increased more 88 dollars in the budget for 1st place cause I will want envelope designs... small and big sizes.

So 1st place is now U$248,00. 

No need to send the envelope designs right now... only the business cards designs.

Thank you.

Industry/Entity Type

Business

Requirements
Must have
• Renata Tavares Vilela

www.RTVimoveis-exemplo.com.br

+554188316402

renata@rtvimoveis-exemplo.com.br

```html
<!DOCTYPE html>
<html lang="pt-BR">
<head>
<meta charset="utf-8">
<title>RTV Imoveis – Business Card</title>
<link rel="stylesheet" href="https://fonts.googleapis.com/css2?family=Arimo:wght@400;700&display=swap">
<style>
  :root {
    --page: #ececec;
    --card-dark: #1f1f1f;
    --card-mid: #5a5a5a;
    --card-light: #f4f4f4;
    --stripe: #6c6c6c;
    --ink: #0d0d0d;
    --ink-soft: #2a1e1e;
  }
  * { margin: 0; padding: 0; box-sizing: border-box; }
  html, body {
    width: 1200px; height: 929px; overflow: hidden;
    background: var(--page);
    font-family: "Arimo", Arial, sans-serif;
  }
  .canvas { position: relative; width: 1200px; height: 929px; }
  .card {
    position: absolute; width: 640px; height: 360px; overflow: hidden;
    box-shadow: 0 6px 18px rgba(0,0,0,.35);
  }
  .card svg.card-art { position: absolute; inset: 0; }
  .card-back { left: 60px; top: 60px; }
  .card-front { left: 500px; top: 480px; }

  .wordmark { position: absolute; font-weight: 700; color: var(--ink); letter-spacing: 1px; line-height: 1; }
  .card-back .wordmark { left: 215px; top: 95px; font-size: 92px; }
  .card-back .website {
    position: absolute; left: 255px; top: 228px;
    font-size: 18px; color: #1b1b1b;
  }
  .card-front .wordmark-small { left: 128px; top: 52px; font-size: 32px; }
  .card-front .wordmark-large { left: 462px; top: 98px; font-size: 50px; }
  .card-front .company {
    position: absolute; left: 100px; top: 110px;
    font-size: 29px; color: var(--ink-soft);
  }
  .contact {
    position: absolute; left: 34px; top: 296px;
    font-size: 17px; line-height: 22px; color: var(--ink);
    list-style: none;
  }
</style>
</head>
<body>
<main class="canvas">

  <section class="card card-back" aria-label="Business card back">
    <svg class="card-art" width="640" height="360" viewBox="0 0 640 360">
      <defs>
        <radialGradient id="backGlow" cx="300" cy="190" r="330" gradientUnits="userSpaceOnUse">
          <stop offset="0" stop-color="#f2f2f2"/>
          <stop offset=".45" stop-color="#6e6e6e"/>
          <stop offset="1" stop-color="var(--card-dark)"/>
        </radialGradient>
        <linearGradient id="backBand" x1="0" y1="0" x2="1" y2="0">
          <stop offset="0" stop-color="#4a4a4a"/>
          <stop offset=".5" stop-color="#9a9a9a"/>
          <stop offset="1" stop-color="#3a3a3a"/>
        </linearGradient>
        <linearGradient id="backFoot" x1="0" y1="0" x2="1" y2="0">
          <stop offset="0" stop-color="#ffffff"/>
          <stop offset="1" stop-color="#8a8a8a"/>
        </linearGradient>
      </defs>
      <rect width="640" height="360" fill="url(#backGlow)"/>
      <rect y="206" width="640" height="16" fill="var(--stripe)"/>
      <rect y="222" width="640" height="84" fill="url(#backBand)"/>
      <rect y="306" width="640" height="54" fill="url(#backFoot)"/>
    </svg>
    <p class="wordmark">RTV</p>
    <p class="website">www.RTVimoveis-exemplo.com.br</p>
  </section>

  <section class="card card-front" aria-label="Business card front">
    <svg class="card-art" width="640" height="360" viewBox="0 0 640 360">
      <defs>
        <radialGradient id="frontGlow" cx="330" cy="215" r="340" gradientUnits="userSpaceOnUse">
          <stop offset="0" stop-color="#f6f6f6"/>
          <stop offset=".4" stop-color="#808080"/>
          <stop offset="1" stop-color="var(--card-dark)"/>
        </radialGradient>
        <linearGradient id="frontBand" x1="0" y1="0" x2="1" y2="0">
          <stop offset="0" stop-color="#555"/>
          <stop offset=".5" stop-color="#8e8e8e"/>
          <stop offset="1" stop-color="#3c3c3c"/>
        </linearGradient>
        <linearGradient id="frontFoot" x1="0" y1="0" x2="1" y2="0">
          <stop offset="0" stop-color="#ffffff"/>
          <stop offset=".6" stop-color="#dcdcdc"/>
          <stop offset="1" stop-color="#8c8c8c"/>
        </linearGradient>
        <linearGradient id="arcShade" x1="0" y1="0" x2="1" y2="0">
          <stop offset="0" stop-color="#000"/>
          <stop offset=".8" stop-color="#1a1a1a"/>
          <stop offset="1" stop-color="#000"/>
        </linearGradient>
      </defs>
      <rect width="640" height="360" fill="url(#frontGlow)"/>
      <path class="sweep-arc" d="M395 0 C470 70 430 190 220 214 C120 225 40 215 0 200 L0 180 C60 200 160 205 240 192 C390 168 420 80 370 0 Z" fill="url(#arcShade)"/>
      <rect y="248" width="640" height="16" fill="var(--stripe)"/>
      <rect y="264" width="640" height="24" fill="url(#frontBand)"/>
      <rect y="288" width="640" height="72" fill="url(#frontFoot)"/>
    </svg>
    <p class="wordmark wordmark-small">RTV</p>
    <p class="company">IMOVEIS</p>
    <p class="wordmark wordmark-large">RTV</p>
    <ul class="contact">
      <li>Name:Renata Tavares Vilela</li>
      <li>Email:renata@rtvimoveis-exemplo.com.br</li>
      <li>Number:+554188316402</li>
    </ul>
  </section>

</main>
</body>
</html>
```